New Business Cards for Parvel

About Parvel:
At Parvel, we're more than just a company—we're a force for positive change in the staffing industry. Our brand is our heartbeat, and we need a designer who can translate that into every design element.

The Project:
We're revamping our business cards and need your artistic flair to make them stand out. Here's what we're looking for:

- Incorporate our existing brand elements (logo, colours, fonts) into the design.
- Craft a design that's sleek, professional, and memorable.
- Provide options for different layouts and finishes.
- Collaborate closely with our team to ensure the final product exceeds expectations.

Please note: For general text, we use Avenir. The brand guidelines are slightly out of date and don't have correct imaging. Colours are correct though.

```html
<!DOCTYPE html>
<html lang="en">
<head>
<meta charset="utf-8">
<title>Parvel Business Cards</title>
<link href="https://fonts.googleapis.com/css2?family=Mulish:wght@400;800&display=swap" rel="stylesheet">
<style>
  :root {
    --backdrop: #8b8b89;
    --paper: #ffffff;
    --plum: #4b1f5c;
    --plum-ink: #4a1a5e;
    --plum-soft: #5e2f72;
    --magenta: #e5177b;
    --grey-text: #5c5c66;
    --rule: #6d4a7c;
  }
  * { margin: 0; padding: 0; box-sizing: border-box; }
  html, body {
    width: 1200px; height: 801px; overflow: hidden;
    background: var(--backdrop);
    font-family: "Mulish", "Avenir", sans-serif;
  }
  .sheet {
    position: relative; width: 1200px; height: 801px;
    display: flex; align-items: center; justify-content: center; gap: 40px;
  }
  .card {
    position: relative; width: 540px; height: 308px;
    border-bottom: 4px solid var(--magenta);
    box-shadow: 0 6px 18px rgba(0,0,0,0.25);
    overflow: hidden;
  }

  /* Front */
  .card-front { background: var(--paper); display: flex; align-items: center; }
  .front-brand { display: flex; align-items: center; gap: 12px; padding-left: 34px; width: 262px; }
  .brand-mark { width: 40px; height: 40px; background: var(--plum-ink); flex: none; }
  .brand-name {
    font-weight: 800; color: var(--plum-ink); font-size: 44px;
    letter-spacing: -0.5px; line-height: 1;
  }
  .tagline { color: var(--plum-ink); font-size: 12px; margin-top: 4px; }
  .divider { width: 1px; height: 118px; background: var(--rule); margin: 0 24px 0 0; }
  .contact-block { color: var(--grey-text); }
  .person-name { color: var(--plum-ink); font-weight: 800; font-size: 21px; line-height: 1.2; }
  .person-title { font-size: 13px; margin-bottom: 14px; }
  .contact-list { list-style: none; font-size: 12.5px; }
  .contact-list li { display: flex; align-items: center; gap: 8px; margin-bottom: 5px; }
  .contact-list svg { width: 11px; height: 11px; fill: var(--magenta); flex: none; }

  /* Back */
  .card-back { background: var(--plum); }
  .back-placeholder {
    position: absolute; left: 60px; top: 70px; width: 150px; height: 170px;
    background: linear-gradient(160deg, var(--plum-soft), var(--plum));
    opacity: 0.8;
  }
  .back-brand { position: absolute; right: 48px; top: 104px; color: var(--paper); }
  .back-brand .brand-name { color: var(--paper); font-size: 80px; letter-spacing: -1.5px; }
  .back-brand .tagline { color: var(--paper); font-size: 20px; margin-top: 8px; padding-left: 4px; }
</style>
</head>
<body>
<main class="sheet">
  <section class="card card-front">
    <div class="front-brand">
      <span class="brand-mark" aria-hidden="true"></span>
      <div>
        <div class="brand-name">Parvel</div>
        <p class="tagline">people first, always</p>
      </div>
    </div>
    <div class="divider"></div>
    <div class="contact-block">
      <h1 class="person-name">Dana Whitlock</h1>
      <p class="person-title">President</p>
      <ul class="contact-list">
        <li><svg viewBox="0 0 24 24" aria-hidden="true"><path d="M6.6 10.8a15 15 0 0 0 6.6 6.6l2.2-2.2a1 1 0 0 1 1-.25 11.4 11.4 0 0 0 3.6.57 1 1 0 0 1 1 1V20a1 1 0 0 1-1 1A17 17 0 0 1 3 4a1 1 0 0 1 1-1h3.5a1 1 0 0 1 1 1c0 1.25.2 2.45.57 3.57a1 1 0 0 1-.25 1z"/></svg>555-014-2290</li>
        <li><svg viewBox="0 0 24 24" aria-hidden="true"><path d="M2 5h20v14H2zm2 2v.5l8 5 8-5V7z"/></svg>d.whitlock@parvel.com.au</li>
        <li><svg viewBox="0 0 24 24" aria-hidden="true"><circle cx="12" cy="12" r="10"/><path d="M2 12h20M12 2c3 3 3 17 0 20M12 2c-3 3-3 17 0 20" stroke="#fff" stroke-width="1.5" fill="none"/></svg>www.parvel.com.au</li>
      </ul>
    </div>
  </section>
  <section class="card card-back">
    <div class="back-placeholder" role="img" aria-label="Faint brand decoration area"></div>
    <div class="back-brand">
      <div class="brand-name">Parvel</div>
      <p class="tagline">people first, always</p>
    </div>
  </section>
</main>
</body>
</html>
```